Accountant & CPA Website $100 bonus

We are designing a website for our client Willowmere Accountants and CPAs. They are a new business and looking for a clean, modern website. The services they offer are siilar to: https://www.brx-tal.com/index.htm

We would like to see designs that use the black and the green mostly, with a hint of purple and grey. However, we do like to give our designers the freedom to be creative. If you see a different vison, feel free to express that.

Number of Pages Required

1 page

Font styles to use
Sans Serif

```html
<!DOCTYPE html>
<html lang="en">
<head>
<meta charset="utf-8">
<title>Willowmere Accountants and CPAs</title>
<link href="https://fonts.googleapis.com/css2?family=Lato:wght@400;700;900&family=Merriweather:wght@700;900&display=swap" rel="stylesheet">
<style>
:root{
  --black:#000;
  --panel:#111;
  --card:#1a1a1a;
  --green:#7f9c23;
  --purple:#3a17a5;
  --link:#4b2ad0;
  --grey:#8a8a8a;
  --light:#cfcfcf;
  --white:#fff;
}
*{margin:0;padding:0;box-sizing:border-box}
html,body{width:1200px;height:3985px;overflow:hidden;background:var(--black)}
body{position:relative;font-family:'Lato',sans-serif;color:var(--white)}
.section{position:absolute;left:0;width:1200px;overflow:hidden}
.abs{position:absolute}
.serif{font-family:'Merriweather',serif;font-weight:900}
.btn{position:absolute;display:flex;align-items:center;justify-content:center;gap:10px;border-radius:30px;background:var(--purple);color:var(--white);font-weight:700;font-size:13px;text-transform:uppercase;white-space:nowrap}
.btn .ico{width:13px;height:13px}
.eyebrow{position:absolute;color:var(--green);font-size:17px;text-transform:uppercase;display:flex;align-items:center;gap:14px}
.eyebrow .rule{width:44px;height:1px;background:var(--grey)}
.center{left:0;width:1200px;justify-content:center;text-align:center}
.heading{position:absolute;color:#7a7a7a;font-size:36px;text-transform:uppercase;letter-spacing:.5px}

/* header */
.site-header{top:0;height:134px;background:var(--black);border-bottom:4px solid var(--green)}
.brand{position:absolute;left:111px;top:46px;display:flex;align-items:center;gap:10px;font-size:28px;font-weight:900;color:var(--green);letter-spacing:1px;white-space:nowrap}
.brand .mark{width:22px;height:22px;border-radius:50%;background:var(--purple);flex:none}
.nav{position:absolute;left:424px;top:57px;display:flex;gap:25px;font-size:14px;font-weight:700;white-space:nowrap}
.nav .active{color:var(--green)}

/* hero */
.hero{top:134px;height:600px}
.hero-photo{position:absolute;inset:0;background:linear-gradient(100deg,#1d2622 0%,#3f4a44 35%,#8d8f88 60%,#5b5249 80%,#2c2622 100%)}
.hero-shade{position:absolute;inset:0;background:linear-gradient(90deg,rgba(0,0,0,.55),rgba(0,0,0,.1) 60%)}
.social-rail .dot{position:absolute;border-radius:50%}
.slider-dots{position:absolute;left:560px;top:568px;display:flex;gap:6px}
.slider-dots span{width:11px;height:11px;border-radius:50%;border:1px solid #ddd}
.slider-dots .on{background:var(--green);border-color:var(--green)}

/* about */
.about{top:734px;height:670px;background:var(--black)}
.about p{font-size:13.5px;line-height:25.6px;text-align:justify}

/* services */
.services{top:1404px;height:702px;background:var(--panel)}
.svc{position:absolute;top:207px;width:308px;height:406px;background:var(--black);text-align:center}
.svc.featured{background:var(--purple)}
.svc .img{height:201px}
.svc h3{margin-top:24px;font-size:17px;font-weight:900;text-transform:uppercase}
.svc p{margin:10px 12px 0;font-size:13px;line-height:25px;color:#ddd}
.svc .btn{left:86px;top:345px;width:137px;height:45px}
.svc.featured .btn{background:var(--white);color:#111}
.arrow-circle{position:absolute;width:36px;height:36px;border-radius:50%;display:flex;align-items:center;justify-content:center}

/* banner */
.banner{top:2107px;height:470px}
.banner-photo{position:absolute;inset:0;background:linear-gradient(90deg,#2f3528 0%,#6d6a55 40%,#4d4d45 65%,#2b2a24 100%)}
.bubble{position:absolute;left:111px;top:63px;width:344px;height:344px;border-radius:50%;background:rgba(255,255,255,.92);text-align:center}

/* reviews */
.reviews{top:2577px;height:484px;background:var(--black)}
.review{position:absolute;top:178px;width:308px;height:230px;background:var(--card)}
.avatar{position:absolute;left:26px;top:34px;width:62px;height:62px;border-radius:50%;background:linear-gradient(#9aa4ad,#4b5560);border:2px solid #eee}
.stars{position:absolute;left:114px;top:36px;color:#f2b705;font-size:10px;letter-spacing:1px}
.review h4{position:absolute;left:114px;top:50px;font-size:17px;font-weight:700}
.review .date{position:absolute;left:114px;top:78px;font-size:9px;color:#bbb}
.review p{position:absolute;left:25px;top:112px;width:258px;font-size:13px;line-height:22px;color:#777;text-align:justify}

/* blog */
.blog{top:3061px;height:609px;background:var(--panel)}
.post-card{position:absolute;top:183px;height:358px;background:var(--card)}
.post-date{color:var(--green);font-size:13px;font-weight:700}
.post-title{font-size:15px;font-weight:900;line-height:23px}
.post-text{font-size:12.5px;line-height:22px;color:#bbb}
.read-more{display:flex;align-items:center;gap:10px;color:var(--link);font-size:15px}

/* footer */
.site-footer{top:3670px;height:315px;background:var(--black)}
.foot-col{position:absolute;top:50px}
.foot-col h5{font-size:15px;color:var(--grey);font-weight:700;text-transform:uppercase;display:inline-block;border-bottom:1px solid var(--grey);padding-bottom:3px}
.foot-col ul{list-style:none;margin-top:20px}
.foot-col li{display:flex;align-items:flex-start;gap:16px;font-size:14px;height:32.5px;white-space:nowrap}
.foot-col li svg{flex:none;margin-top:2px}
.foot-social span{position:absolute;top:163px;width:30px;height:30px;border-radius:50%;border:1px solid #ddd}
</style>
</head>
<body>

<svg width="0" height="0" style="position:absolute">
  <defs>
    <symbol id="play" viewBox="0 0 14 14"><circle cx="7" cy="7" r="7" fill="currentColor"/><path d="M5.5 4l4 3-4 3z" fill="var(--purple)"/></symbol>
    <symbol id="go" viewBox="0 0 14 14"><circle cx="7" cy="7" r="6" fill="none" stroke="currentColor" stroke-width="2"/><path d="M6 4.5l2.5 2.5L6 9.5" fill="none" stroke="currentColor" stroke-width="1.6"/></symbol>
  </defs>
</svg>

<header class="section site-header">
  <div class="brand"><span class="mark"></span>WILLOWMERE</div>
  <nav class="nav">
    <span class="active">HOME</span><span>ABOUT US</span><span>SERVICES</span><span>INSIGHTS &amp; NEWS</span><span>CONTACT US</span>
  </nav>
  <div class="btn" style="left:934px;top:40px;width:153px;height:50px"><svg class="ico" style="color:#fff"><use href="#play"/></svg>GET STARTED</div>
</header>

<section class="section hero">
  <div class="hero-photo" role="img" aria-label="Two business people reviewing documents and a phone at an office desk"></div>
  <div class="hero-shade"></div>
  <div class="abs" style="left:111px;top:137px;color:var(--green);font-size:17px">WILLOWMERE ACCOUNTANTS AND CPAS</div>
  <h1 class="abs serif" style="left:111px;top:176px;font-size:38px;line-height:47px">TAX &amp; ACCOUNTING<br>SERVICES FOR BUSINESSES<br>&amp; INDIVIDUALS</h1>
  <p class="abs" style="left:111px;top:328px;width:450px;font-size:15px;line-height:26px">Lorem ipsum dolor sit amet, consectetur adipiscing elit sed do eiusmod tempor incididunt ut laborea.</p>
  <div class="btn" style="left:111px;top:412px;width:153px;height:48px"><svg class="ico" style="color:#fff"><use href="#play"/></svg>LEARN MORE</div>
  <div class="social-rail">
    <span class="dot" style="top:231px;left:41px;width:36px;height:36px;border:1px solid #ddd"></span>
    <span class="dot" style="top:280px;left:54px;width:10px;height:10px;background:#ddd"></span>
    <span class="dot" style="top:319px;left:54px;width:10px;height:10px;background:#ddd"></span>
    <span class="dot" style="top:358px;left:54px;width:10px;height:10px;border:1px solid #ddd"></span>
  </div>
  <div class="abs" style="left:59px;top:398px;width:1px;height:74px;background:#ddd"></div>
  <div class="abs" style="left:52px;top:562px;transform:rotate(-90deg);transform-origin:left top;font-size:9px;white-space:nowrap">SCROLL DOWN</div>
  <div class="abs" style="left:51px;top:590px;width:16px;height:16px;border-radius:50%;background:var(--green)"></div>
  <div class="slider-dots"><span></span><span class="on"></span><span></span><span></span><span></span></div>
</section>
<svg class="abs" style="left:52px;top:726px" width="14" height="30" viewBox="0 0 14 30"><path d="M7 0v26M1 20l6 7 6-7" fill="none" stroke="#fff" stroke-width="1.6"/></svg>

<section class="section about">
  <div class="abs" style="left:99px;top:87px;width:145px;height:145px;background:var(--green)"></div>
  <div class="abs" style="left:128px;top:115px;width:412px;height:434px;background:linear-gradient(135deg,#e8e9ea,#bfc4c8 50%,#8c9aa9)" role="img" aria-label="Accountant working with a calculator and paperwork at a desk"></div>
  <div class="abs" style="left:445px;top:453px;width:124px;height:124px;background:rgba(255,255,255,.08)" role="img" aria-label="Dotted decoration"></div>
  <div class="eyebrow" style="left:600px;top:142px"><span class="rule"></span>ABOUT US</div>
  <h2 class="heading serif" style="left:600px;top:182px;font-size:29px;line-height:40px">FORGET EVERYTHING YOU<br>KNOW ABOUT ACCOUNTING</h2>
  <p class="abs" style="left:600px;top:280px;width:488px">Lorem ipsum dolor sit amet, consectetur adipiscing elit, sed do eiusmod tempor incididunt ut labore et dolore magna aliqua. Ut enim ad minim veniam, quis nostrud exercitation ullamco laboris nisi ut aliquip ex ea commodo consequat. Duis aute irure dolor in reprehenderit in voluptate velit esse cillum dolore eu fugiat nulla pariatur. Excepteur sint occaecat cupidatat non proident, sunt in culpa qui officia deserunt mollit anim id est laborum.</p>
  <div class="btn" style="left:600px;top:467px;width:153px;height:48px"><svg class="ico" style="color:#fff"><use href="#play"/></svg>LEARN MORE</div>
</section>

<section class="section services">
  <div class="eyebrow center" style="top:80px"><span class="rule"></span>WHAT WE DO<span class="rule"></span></div>
  <h2 class="heading serif center" style="top:116px">SERVICES OFFERD</h2>
  <article class="svc" style="left:111px">
    <div class="img" style="background:linear-gradient(135deg,#d9dde2,#7e8894 60%,#3c434b)" role="img" aria-label="Laptop with floating tax icons"></div>
    <h3>TAX SERVICES</h3>
    <p>Lorem ipsum dolor sit amet, consectetur adipi scing elit, sed do eiusmod tempor incididunt ut labore et dolore magna aliqua.</p>
    <div class="btn"><svg class="ico" style="color:#fff"><use href="#play"/></svg>LEARN MORE</div>
  </article>
  <article class="svc featured" style="left:445px">
    <div class="img" style="background:linear-gradient(135deg,#f0d2a5,#a98a6a 45%,#7d8fa3)" role="img" aria-label="Team reviewing charts on a desk with a laptop"></div>
    <h3>ACCOUNTING SERVICES</h3>
    <p>Lorem ipsum dolor sit amet, consectetur adipi scing elit, sed do eiusmod tempor incididunt ut labore et dolore magna aliqua.</p>
    <div class="btn"><svg class="ico" style="color:#111"><use href="#play"/></svg>LEARN MORE</div>
  </article>
  <article class="svc" style="left:779px">
    <div class="img" style="background:radial-gradient(circle at 35% 40%,#f2a046,#7a4527 35%,#1e2a36 75%)" role="img" aria-label="Glowing light bulb in a hand beside a laptop"></div>
    <h3>NICHE INDUSTRIES</h3>
    <p>Lorem ipsum dolor sit amet, consectetur adipi scing elit, sed do eiusmod tempor incididunt ut labore et dolore magna aliqua.</p>
    <div class="btn"><svg class="ico" style="color:#fff"><use href="#play"/></svg>LEARN MORE</div>
  </article>
  <div class="arrow-circle" style="left:39px;top:396px;background:#fff"><svg width="10" height="12"><path d="M7 1L2 6l5 5" fill="none" stroke="#111" stroke-width="2"/></svg></div>
  <div class="arrow-circle" style="left:1123px;top:396px;background:var(--green)"><svg width="10" height="12"><path d="M3 1l5 5-5 5" fill="none" stroke="#fff" stroke-width="2"/></svg></div>
</section>

<section class="section banner">
  <div class="banner-photo" role="img" aria-label="Laptop and tablet with financial charts on a wooden table"></div>
  <div class="bubble">
    <div class="eyebrow" style="left:0;width:344px;justify-content:center;top:68px"><span class="rule"></span>GET STARTED<span class="rule"></span></div>
    <h2 class="heading serif" style="left:0;width:344px;top:104px;font-size:22px;line-height:32px">WE ARE SPECIALIZE IN<br>UNIQUE ACCOUNTING</h2>
    <p class="abs" style="left:22px;width:300px;top:178px;font-size:13px;line-height:23px;color:#888">Lorem ipsum dolor sit amet, consectetur adipisc ing elit, sed do eiusmod temporea.</p>
    <div class="btn" style="left:96px;top:247px;width:153px;height:49px"><svg class="ico" style="color:#fff"><use href="#play"/></svg>GET STARTED</div>
  </div>
</section>

<section class="section reviews">
  <div class="eyebrow center" style="top:62px"><span class="rule"></span>REVIEWS<span class="rule"></span></div>
  <h2 class="heading serif center" style="top:100px;font-size:34px">WHAT OUR CUSTOMERS SAY</h2>
  <article class="review" style="left:111px"><div class="avatar" role="img" aria-label="Customer portrait"></div><div class="stars">★★★★★</div><h4>Jordan Reyes</h4><div class="date">March 2022</div><p>Lorem ipsum dolor sit amet, consectetur adipiscing elit, sed do eiusmod tempor incididunt ut labore et dolore magna aliqua. Ut enim ad minim veniamea.</p></article>
  <article class="review" style="left:445px"><div class="avatar" role="img" aria-label="Customer portrait"></div><div class="stars">★★★★★</div><h4>Jordan Reyes</h4><div class="date">March 2022</div><p>Lorem ipsum dolor sit amet, consectetur adipiscing elit, sed do eiusmod tempor incididunt ut labore et dolore magna aliqua. Ut enim ad minim veniamea.</p></article>
  <article class="review" style="left:779px"><div class="avatar" role="img" aria-label="Customer portrait"></div><div class="stars">★★★★★</div><h4>Jordan Reyes</h4><div class="date">March 2022</div><p>Lorem ipsum dolor sit amet, consectetur adipiscing elit, sed do eiusmod tempor incididunt ut labore et dolore magna aliqua. Ut enim ad minim veniamea.</p></article>
  <svg class="abs" style="left:48px;top:286px" width="26" height="14"><path d="M25 7H2M8 1L2 7l6 6" fill="none" stroke="#555" stroke-width="1.6"/></svg>
  <svg class="abs" style="left:1126px;top:286px" width="26" height="14"><path d="M1 7h23M18 1l6 6-6 6" fill="none" stroke="#fff" stroke-width="1.6"/></svg>
</section>

<section class="section blog">
  <div class="eyebrow center" style="top:72px"><span class="rule"></span>BLOG<span class="rule"></span></div>
  <h2 class="heading serif center" style="top:108px;font-size:32px">SUCCESS STORIES</h2>
  <article class="post-card" style="left:111px;width:478px">
    <div class="abs" style="left:17px;top:18px;width:444px;height:206px;background:linear-gradient(135deg,#e6e8ea,#9aa1a8 50%,#3a4048)" role="img" aria-label="Hands using a calculator beside a laptop with a rising chart"></div>
    <div class="abs post-date" style="left:38px;top:240px">30 MAY 2022</div>
    <div class="abs post-title" style="left:38px;top:265px;width:410px">Lorem ipsum dolor sit amet, consectetur adipiscing elit sed do eiusmod tempor inciea.</div>
    <div class="abs read-more" style="left:38px;top:318px">Read More <svg width="14" height="14" style="color:var(--link)"><use href="#go"/></svg></div>
  </article>
  <article class="post-card" style="left:611px;width:476px">
    <div class="abs" style="left:18px;top:20px;width:152px;height:148px;background:linear-gradient(135deg,#cfc7bd,#6d6358 55%,#2f3238)" role="img" aria-label="Colleagues discussing work at a desk"></div>
    <div class="abs post-date" style="left:188px;top:33px">30 MAY 2022</div>
    <div class="abs post-title" style="left:188px;top:56px;width:270px">Lorem ipsum dolor sit amet consec tetur adipiscing eliea.</div>
    <div class="abs post-text" style="left:188px;top:104px;width:270px">Sed ut perspiciatis unde omnis iste natus err or sit voluptatem accusa.</div>
    <div class="abs read-more" style="left:188px;top:150px">Read More <svg width="14" height="14" style="color:var(--link)"><use href="#go"/></svg></div>
    <div class="abs" style="left:18px;top:191px;width:152px;height:148px;background:linear-gradient(135deg,#d9d4cb,#7b7266 55%,#33353a)" role="img" aria-label="Two people reviewing a document"></div>
    <div class="abs post-date" style="left:188px;top:205px">30 MAY 2022</div>
    <div class="abs post-title" style="left:188px;top:228px;width:270px">Lorem ipsum dolor sit amet consec tetur adipiscing eliea.</div>
    <div class="abs post-text" style="left:188px;top:276px;width:270px">Sed ut perspiciatis unde omnis iste natus err or sit voluptatem accusa.</div>
    <div class="abs read-more" style="left:188px;top:322px">Read More <svg width="14" height="14" style="color:var(--link)"><use href="#go"/></svg></div>
  </article>
</section>

<footer class="section site-footer">
  <div class="brand" style="top:100px"><span class="mark"></span>WILLOWMERE</div>
  <div class="foot-social"><span style="left:147px;background:var(--purple);border-color:var(--purple)"></span><span style="left:183px"></span><span style="left:218px"></span><span style="left:254px"></span></div>
  <div class="foot-col" style="left:430px">
    <h5>Navigation</h5>
    <ul>
      <li><svg width="14" height="14" style="color:var(--green)"><use href="#go"/></svg>Home</li>
      <li><svg width="14" height="14" style="color:var(--green)"><use href="#go"/></svg>About Us</li>
      <li><svg width="14" height="14" style="color:var(--green)"><use href="#go"/></svg>Services</li>
      <li><svg width="14" height="14" style="color:var(--green)"><use href="#go"/></svg>Insights &amp; News</li>
      <li><svg width="14" height="14" style="color:var(--green)"><use href="#go"/></svg>Contact Us</li>
    </ul>
  </div>
  <div class="foot-col" style="left:626px">
    <h5>Services</h5>
    <ul>
      <li><svg width="14" height="14" style="color:var(--green)"><use href="#go"/></svg>Tax Services</li>
      <li><svg width="14" height="14" style="color:var(--green)"><use href="#go"/></svg>Accounting Services</li>
      <li><svg width="14" height="14" style="color:var(--green)"><use href="#go"/></svg>Niche Industries</li>
      <li><svg width="14" height="14" style="color:var(--green)"><use href="#go"/></svg>Cloud Ledger Accounting</li>
    </ul>
  </div>
  <div class="foot-col" style="left:886px">
    <h5>Contact</h5>
    <ul>
      <li style="height:58px"><svg width="12" height="16" viewBox="0 0 12 16"><path d="M6 0a6 6 0 0 0-6 6c0 4.5 6 10 6 10s6-5.5 6-10a6 6 0 0 0-6-6z" fill="var(--green)"/><circle cx="6" cy="6" r="2.2" fill="#000"/></svg><span>218 Alder Lane,<br>Springfield</span></li>
      <li style="height:36px"><svg width="14" height="14" viewBox="0 0 14 14"><path d="M3 1l2.5 3-1.5 1.5a8 8 0 0 0 4.5 4.5L10 8.5l3 2.5-1.5 2.5C6 13 1 8 .5 2.5z" fill="var(--green)"/></svg>+1 (555) 014 2290</li>
      <li><svg width="16" height="12" viewBox="0 0 16 12"><rect width="16" height="12" rx="1" fill="var(--green)"/><path d="M1 1l7 6 7-6" fill="none" stroke="#000" stroke-width="1.3"/></svg>info@willowmere.com</li>
    </ul>
  </div>
  <div class="abs" style="left:111px;top:257px;width:976px;height:1px;background:#444"></div>
  <svg class="abs" style="left:1066px;top:226px" width="20" height="44" viewBox="0 0 20 44"><path d="M10 2v28M4 8l6-6 6 6" fill="none" stroke="#fff" stroke-width="1.6"/><circle cx="10" cy="34" r="8" fill="var(--green)"/></svg>
  <div class="abs" style="left:430px;top:270px;font-size:11px">© 2023 WILLOWMERE ACCOUNTANTS AND CPAS &nbsp;- &nbsp;All Rights Reserved</div>
</footer>

</body>
</html>
```